Collection of baby & child print designs.

We require a collection of designs that can be edited and customised in Adobe Illustrator/InDesign so that they can be personalised for our customers.

The designs can be of anything, but must include a child's name, date of birth, or location of birth (basically any personal identifier) or a combination of the above.

A range of examples of similar products can be found here - http://qvx.zt/8Rkwp

Our designs can take influence from the examples on this site, but must be different.

We require a range of options for both boys and girls.

Reason: For amends to be made to some designs.

Target Market(s)

Parents, Friends of parents, people looking for a unique gift.

Industry/Entity Type

Baby

Requirements
Must have
• Must fit within the printable area of an A3 page.

```html
<!DOCTYPE html>
<html lang="en">
<head>
<meta charset="utf-8">
<title>Ruby – Birth Print</title>
<link href="https://fonts.googleapis.com/css2?family=Playfair+Display:wght@400;500;700;800;900&display=swap" rel="stylesheet">
<style>
  :root {
    --pink: #e8527f;
    --pink-soft: #f091a8;
    --grey: #6d6e71;
    --teal: #8fd2c4;
    --paper: #ffffff;
  }
  html, body {
    margin: 0;
    padding: 0;
    width: 900px;
    height: 1200px;
    overflow: hidden;
    background: var(--paper);
  }
  .birth-print {
    display: block;
    width: 900px;
    height: 1200px;
  }
  .birth-print text {
    font-family: "Playfair Display", "Bodoni Moda", serif;
  }
  .first-name { fill: var(--pink); font-size: 300px; font-weight: 700; }
  .rule { fill: var(--grey); }
  .birth-date { fill: var(--teal); font-size: 135px; font-weight: 800; }
  .birth-weight { fill: var(--grey); font-size: 130px; font-weight: 500; }
  .nickname-soft { fill: var(--pink-soft); font-size: 93px; font-weight: 800; }
  .nickname-strong { fill: var(--pink); font-size: 102px; font-weight: 900; }
  .nickname-side { fill: var(--teal); font-size: 102px; font-weight: 700; }
  .birth-time { fill: var(--grey); font-size: 195px; font-weight: 400; }
  .full-name { fill: var(--pink); font-size: 127px; font-weight: 800; }
</style>
</head>
<body>
<svg class="birth-print" viewBox="0 0 900 1200" xmlns="http://www.w3.org/2000/svg" aria-label="Birth announcement print for Ruby Harlow">
  <text class="first-name" x="34" y="236" textLength="832" lengthAdjust="spacingAndGlyphs">RUBY</text>
  <rect class="rule" x="34" y="256" width="832" height="10"/>

  <g transform="translate(132 1032) rotate(-90)">
    <text class="birth-date" x="0" y="0" textLength="744" lengthAdjust="spacingAndGlyphs">01.10.2012</text>
  </g>

  <text class="birth-weight" x="154" y="396" textLength="712" lengthAdjust="spacingAndGlyphs">7lbs11.5oz</text>

  <text class="nickname-soft" x="180" y="498" textLength="454" lengthAdjust="spacingAndGlyphs">MAMMY’S</text>
  <text class="nickname-soft" x="180" y="612" textLength="454" lengthAdjust="spacingAndGlyphs">PRINCESS</text>
  <text class="nickname-strong" x="180" y="720" textLength="456" lengthAdjust="spacingAndGlyphs">BUNDLE</text>
  <text class="nickname-strong" x="180" y="804" textLength="454" lengthAdjust="spacingAndGlyphs">OF JOY</text>

  <g transform="translate(744 840) rotate(-90)">
    <text class="nickname-side" x="0" y="0" textLength="426" lengthAdjust="spacingAndGlyphs">LITTLE</text>
  </g>
  <g transform="translate(866 840) rotate(-90)">
    <text class="nickname-side" x="0" y="0" textLength="426" lengthAdjust="spacingAndGlyphs">SMILER</text>
  </g>

  <text class="birth-time" x="168" y="1026" textLength="698" lengthAdjust="spacingAndGlyphs">11:20PM</text>

  <rect class="rule" x="34" y="1052" width="832" height="10"/>
  <text class="full-name" x="34" y="1170" textLength="832" lengthAdjust="spacingAndGlyphs">RUBY HARLOW</text>
</svg>
</body>
</html>
```